Norvale Email Signature Banners – Fabrication Capability Series

www.Norvale.com.au is an Australian engineering and fabrication company specialising in fabrication and welding of :
steel piping spools,
skids and frames,
small volume process steel tanks
and general steel fabrication
We require four distinct banner designs for use in Teldrin Quillmark email signatures. Each banner will highlight a specific capability while maintaining a consistent brand identity.
Deliverables
Four banners total:
Piping Spools Fabrication – focus on precision welding and stainless steel pipework
Skid & Frames Fabrication – highlight skid systems and structural frames
Small Steel Tanks Fabrication – show fabricated tanks and workshop craftsmanship
General Fabrication Solutions – broad steel fabrication theme for company-wide use
Dimensions: 600–700 px wide × 100 px high
Format: PNG (preferred), small file size prefered
Resolution: 72 dpi
Background: non-transparent, industrial or workshop setting
Text examples:
1. Piping Spools Fabrication
Option A: “Expert Fabrication Solutions for Process Piping”
Option B: “Precision Welding for Complex Systems”
Option C: “Delivering Quality in Every Spool”
Option D: “Engineered for Flow, Built for Strength”
2. Skid & Frames Fabrication
Option A: “Custom Engineered Modular Systems”
Option B: “Built Strong. Designed Smart.”
Option C: “Reliable Frames for Industrial Performance”
Option D: “Modular Fabrication for Seamless Integration”
3. Small Steel Tanks Fabrication
Option A: “Precision Built for Your Needs”
Option B: “Compact Strength. Proven Durability.”
Option C: “Fabricated for Performance and Longevity”
Option D: “Small Tanks. Big Reliability.”
4. General Fabrication Solutions
Option A: “Quality Craftsmanship, Proven Results”
Option B: “Your Partner in Precision Fabrication”
Option C: “Engineering Excellence in Every Weld”
Option D: “Australian Fabrication. Global Standards.”
Style Direction
Clean, professional, and engineering‑focused
Use Norvale brand colours
Blend photo realism with vector clarity (no heavy gradients)
Include subtle industrial textures or workshop imagery
Typography: bold sans‑serif, legible at small scale
Usage Context
These banners will appear at the bottom of staff email signatures via Quillmark Email Signature Tool for Teldrin 365, so clarity and fast loading are essential. No Logo is required in the banners.
Reference
Existing Norvale signature is attached. Colour palette to match the signature style and logo.
Target Market(s)
Engineering and construction companies,
Industry/Entity Type
Engineering fabrication design

```html
<!DOCTYPE html>
<html lang="en">
<head>
<meta charset="utf-8">
<title>Norvale Email Signature Banners – Fabrication Capability Series</title>
<link rel="stylesheet" href="https://fonts.googleapis.com/css2?family=Montserrat:wght@700&display=swap">
<style>
  :root {
    --board: #e8e8ea;
    --navy: #001a33;
    --accent: #1ca4e0;
    --ink-light: #f1f1f3;
    --shop-shadow: #141c26;
    --shop-dark: #25313e;
    --steel-mid: #4f5d6b;
    --steel-light: #8d9aa7;
    --steel-bright: #b9c4ce;
    --weld-blue: #5f8fc0;
  }
  * { box-sizing: border-box; margin: 0; padding: 0; }
  html, body {
    width: 1200px;
    height: 800px;
    overflow: hidden;
    background: var(--board);
  }
  .banner-board {
    position: relative;
    width: 1200px;
    height: 800px;
  }
  .banner {
    position: absolute;
    left: 143px;
    width: 914px;
    height: 131px;
    background: var(--navy);
    overflow: hidden;
  }
  .banner--piping  { top: 89px; }
  .banner--frames  { top: 253px; }
  .banner--tanks   { top: 417px; }
  .banner--general { top: 581px; }

  .banner__photo {
    position: absolute;
    left: 0;
    top: 0;
    width: 480px;
    height: 100%;
    -webkit-mask-image: linear-gradient(90deg, #000 0%, #000 62%, rgba(0,0,0,0.35) 82%, rgba(0,0,0,0) 100%);
            mask-image: linear-gradient(90deg, #000 0%, #000 62%, rgba(0,0,0,0.35) 82%, rgba(0,0,0,0) 100%);
  }
  .banner--piping .banner__photo {
    background:
      linear-gradient(180deg, rgba(20,28,38,0.55) 0%, rgba(20,28,38,0) 30%, rgba(20,28,38,0) 70%, rgba(20,28,38,0.6) 100%),
      linear-gradient(100deg, var(--shop-shadow) 0%, var(--shop-dark) 14%, var(--weld-blue) 26%, var(--steel-light) 40%, var(--steel-bright) 52%, var(--steel-mid) 68%, var(--shop-dark) 84%, var(--shop-shadow) 100%);
  }
  .banner--frames .banner__photo {
    background:
      linear-gradient(180deg, #56626f 0%, var(--steel-mid) 22%, var(--shop-dark) 48%, #3a4550 72%, var(--shop-shadow) 100%),
      var(--shop-dark);
  }
  .banner--tanks .banner__photo {
    background:
      linear-gradient(180deg, rgba(20,28,38,0.5) 0%, rgba(20,28,38,0) 35%, rgba(20,28,38,0) 70%, rgba(20,28,38,0.6) 100%),
      linear-gradient(95deg, var(--shop-shadow) 0%, var(--shop-dark) 16%, var(--weld-blue) 28%, var(--steel-light) 42%, var(--steel-bright) 58%, var(--steel-mid) 74%, var(--shop-dark) 90%, var(--shop-shadow) 100%);
  }
  .banner--general .banner__photo {
    background:
      linear-gradient(180deg, rgba(20,28,38,0.45) 0%, rgba(20,28,38,0) 30%, rgba(20,28,38,0) 70%, rgba(20,28,38,0.6) 100%),
      linear-gradient(90deg, var(--steel-mid) 0%, var(--steel-light) 22%, var(--steel-bright) 36%, var(--steel-light) 50%, var(--steel-mid) 64%, var(--shop-dark) 82%, var(--shop-shadow) 100%);
  }

  .banner__headline {
    position: absolute;
    right: 24px;
    top: 17px;
    text-align: right;
    font-family: "Montserrat", sans-serif;
    font-weight: 700;
    font-size: 33px;
    line-height: 47px;
    letter-spacing: 0.3px;
    color: var(--ink-light);
    white-space: nowrap;
  }
  .banner__headline .accent { color: var(--accent); }
</style>
</head>
<body>
<main class="banner-board">

  <section class="banner banner--piping">
    <div class="banner__photo" role="img" aria-label="Welder in a mask welding stainless steel pipe spools with flanges in a workshop, sparks flying"></div>
    <h2 class="banner__headline">
      Precision <span class="accent">Welding</span><br>
      for <span class="accent">Complex Systems</span>
    </h2>
  </section>

  <section class="banner banner--frames">
    <div class="banner__photo" role="img" aria-label="Row of fabricated structural steel skid frames on a workshop floor"></div>
    <h2 class="banner__headline">
      Built <span class="accent">Strong</span><br>
      Designed <span class="accent">Smart</span>
    </h2>
  </section>

  <section class="banner banner--tanks">
    <div class="banner__photo" role="img" aria-label="Welder in a mask welding a small stainless steel tank in a workshop"></div>
    <h2 class="banner__headline">
      Small <span class="accent">Tanks</span><br>
      Big <span class="accent">reliability</span>
    </h2>
  </section>

  <section class="banner banner--general">
    <div class="banner__photo" role="img" aria-label="Stainless steel vessels and flanged pipe sections in a fabrication workshop"></div>
    <h2 class="banner__headline">
      Engineering <span class="accent">Excellence</span><br>
      in Every <span class="accent">Weld</span>
    </h2>
  </section>

</main>
</body>
</html>
```